ONE PAGE WEB DESIGN NEEDED for Finance Company

We need a web design (ONE PAGE DESIGN ONLY) for a new finance website called Brightwell Lending. Brightwell Lending helps customers get the right loan, whether its a home loan, investment loan, business loan etc.

You are required to come up with just the homepage design. Professionalism and quality is the key factors in the successful design.

Here are a few design questions to help you out:

-
What information should be used on the page?
Ive provided a document which outlines all the information needed to put on homepage (attached to the brief - called brightwell_page_info). Also see the Must Have section below on this brief.

-
What links should appear in the navigation/footer?:
The navigation should provide links to the following pages (NOTE: services link has subcategories):
1 Homepage
2 Services
- Home loans
- Investment loans
- Refinancing loans
- Business loans
3 About Us
4 FAQ
5 Contact Us

-
What colors should be used in the design?
Our company colors - Cyan: #2EADE3, Blue: #004B70, White. Feel free to submit designs with slight variations if you feel it improves the design.

-
What should the layout of the page be?
This is up to you to come up with - we are open to different layouts for the page design (as long as they capture the information effectively and making it easy to understand).

Target Market(s)

Potential Home owners, Families and Business Owners

Industry/Entity Type

Business

Requirements
Must have
• - Must contain our logo (attached as PNG and Illustrator file)
- Winning designer must supply a Photoshop file (PSD) that will allow us.
Nice to have
• - Should include photos/images of families, professional groups, tradespeople etc (you can use stock photos from PixQuarry and I will purchase them once you are selected as the winning design)
- Link to a loan calculator somewhere on front page with a button 'Find out how much you could borrow' (or maybe even try adding a loan calculator to the homepage if you think this would look good)
- Page should have a main headline "Finding the right loan for you" or "Brightwell Lending finds the right loan for our customers."
- Must include Accreditation logos somewhere on the homepage (will try and supply these soon)
Should not have
• - Poor quality designs will not be considered
- Do not use clipart

```html
<!DOCTYPE html>
<html lang="en">
<head>
<meta charset="utf-8">
<title>Brightwell Lending — Homepage</title>
<link href="https://fonts.googleapis.com/css2?family=Open+Sans:wght@400;600;700&display=swap" rel="stylesheet">
<style>
:root{
  --cyan:#2eade3;
  --blue:#004b70;
  --ink:#333;
  --muted:#888;
  --line:#e2e2e2;
  --band:#efefef;
  --panel:#e4e4e4;
  --white:#fff;
  --black:#111;
}
*{box-sizing:border-box;margin:0;padding:0}
html,body{width:758px;height:1200px;overflow:hidden;background:var(--white)}
body{font-family:"Open Sans",Arial,sans-serif;color:var(--ink);position:relative}
.site-header{position:absolute;top:0;left:0;width:758px;height:100px}
.brand{position:absolute;left:72px;top:22px;display:flex;align-items:center;gap:10px}
.brand-mark{width:30px;height:30px;border-radius:50%;background:var(--cyan)}
.brand-name{font-size:22px;font-weight:600;color:var(--blue)}
.call{position:absolute;right:72px;top:24px;font-size:9px;color:var(--ink);display:flex;align-items:center;gap:5px}
.call strong{font-weight:700}
.main-nav{position:absolute;right:72px;top:80px;display:flex;gap:18px;font-size:8px;letter-spacing:.5px}
.main-nav a{color:#bbb;text-decoration:none;padding-bottom:4px}
.main-nav a.current{color:var(--ink);border-bottom:2px solid var(--cyan)}
.hero{position:absolute;top:100px;left:0;width:758px;height:265px;border-top:1px solid var(--line);border-bottom:1px solid var(--line)}
.hero-copy{position:absolute;left:75px;top:40px;width:205px;font-size:7.5px;line-height:1.6;color:var(--muted)}
.hero-copy p{margin-bottom:9px}
.btn-primary{display:inline-block;background:var(--cyan);color:var(--white);font-size:7.5px;font-weight:700;padding:6px 16px;text-decoration:none;margin-top:6px}
.hero-photo{position:absolute;left:290px;top:0;width:395px;height:264px;background:linear-gradient(135deg,#f4f6f8 0%,#dfe5ea 55%,#b9c3cc 100%)}
.slide-arrow{position:absolute;top:120px;width:20px;height:20px;border-radius:50%;background:#cfcfcf}
.slide-arrow svg{display:block}
.slide-prev{left:298px}.slide-next{left:660px}
.slide-dots{position:absolute;top:371px;left:0;width:758px;display:flex;justify-content:center;gap:6px}
.slide-dots span{width:7px;height:7px;border-radius:50%;border:1px solid #aaa}
.slide-dots span.on{background:#aaa}
.loan-types{position:absolute;top:420px;left:0;width:758px;text-align:center}
.section-title{font-size:21px;font-weight:600;color:var(--cyan)}
.loan-grid{display:flex;justify-content:center;gap:40px;margin-top:30px}
.loan-col{width:130px;font-size:7.5px;line-height:2.3;color:var(--ink)}
.loan-col h3{font-size:9px;font-weight:700;border-bottom:1px solid var(--line);padding-bottom:5px;margin-bottom:6px}
.contact-band{position:absolute;top:640px;left:0;width:758px;height:225px;background:var(--band);border-top:1px solid var(--line)}
.contact-lead{position:absolute;left:75px;top:52px;width:280px;display:flex;gap:12px}
.phone-icon{flex:0 0 28px;height:28px;border-radius:50%;background:var(--cyan);display:flex;align-items:center;justify-content:center}
.contact-lead h2{font-size:11.5px;font-weight:700;line-height:1.4;color:var(--black)}
.contact-text{position:absolute;left:75px;top:115px;width:260px;font-size:8px;line-height:1.65;color:var(--ink)}
.calculator{position:absolute;left:405px;top:33px;width:290px;height:185px;background:var(--panel);padding:14px 16px}
.calculator h4{font-size:8px;font-weight:700;margin-bottom:14px}
.calc-row{display:flex;align-items:center;font-size:7px;margin-bottom:8px;gap:6px}
.calc-row label{width:62px;white-space:nowrap}
.calc-row .unit{width:10px}
.field{width:40px;height:11px;background:var(--white)}
.field.wide{width:100px}
.calc-row small{font-size:6.5px}
.btn-dark{display:inline-block;background:var(--black);color:var(--white);font-size:7px;font-weight:700;padding:6px 12px;border-radius:10px;margin-top:4px}
.featured{position:absolute;top:945px;left:75px;width:620px}
.featured h3{font-size:9px;font-weight:700;margin-bottom:30px}
.partners{display:flex;justify-content:space-between;align-items:center}
.partner{font-size:20px;font-weight:600;color:#444}
.site-footer{position:absolute;top:1150px;left:0;width:758px;border-top:1px solid var(--line)}
.copyright{position:absolute;left:75px;top:12px;font-size:6.5px;color:var(--muted)}
.social{position:absolute;right:70px;top:10px;display:flex;gap:6px}
.social span{width:10px;height:10px;border-radius:50%;background:#ccc}
</style>
</head>
<body>
<header class="site-header">
  <div class="brand"><span class="brand-mark"></span><span class="brand-name">Brightwell Lending</span></div>
  <div class="call">
    <svg width="10" height="10" viewBox="0 0 24 24"><path fill="#333" d="M6.6 10.8a15 15 0 0 0 6.6 6.6l2.2-2.2c.3-.3.7-.4 1-.2 1.1.4 2.3.6 3.6.6.6 0 1 .4 1 1V20c0 .6-.4 1-1 1A17 17 0 0 1 3 4c0-.6.4-1 1-1h3.5c.6 0 1 .4 1 1 0 1.3.2 2.5.6 3.6.1.3 0 .7-.2 1z"/></svg>
    <span>CALL <strong>1800 555 214</strong> to find out more</span>
  </div>
  <nav class="main-nav">
    <a class="current" href="#">HOMEPAGE</a><a href="#">SERVICES</a><a href="#">ABOUT US</a><a href="#">FAQ</a><a href="#">CONTACT US</a>
  </nav>
</header>

<section class="hero">
  <div class="hero-copy">
    <p>At Brightwell Lending we work hard to find the right loan for our customers. We do that because we are backed by sound industry knowledge, professional experience and a great customer service approach.</p>
    <p>Brightwell Lending guarantees that we will always search for the best solution for your individual lending needs. We can do that because we have access to a wide variety of lending options from major banks to non-bank lenders and we are committed to finding the right lending product for you.</p>
    <a class="btn-primary" href="#">LEARN MORE</a>
  </div>
  <div class="hero-photo" role="img" aria-label="Stock photo of a smiling professional in a suit with colleagues behind him"></div>
  <span class="slide-arrow slide-prev"><svg width="20" height="20" viewBox="0 0 20 20"><path d="M12 6l-4 4 4 4" stroke="#fff" stroke-width="2" fill="none"/></svg></span>
  <span class="slide-arrow slide-next"><svg width="20" height="20" viewBox="0 0 20 20"><path d="M8 6l4 4-4 4" stroke="#fff" stroke-width="2" fill="none"/></svg></span>
</section>
<div class="slide-dots"><span></span><span class="on"></span><span></span></div>

<section class="loan-types">
  <h2 class="section-title">Finding the right loan for you.</h2>
  <div class="loan-grid">
    <div class="loan-col"><h3>HOME LOAN</h3><div>Home buyers</div><div>First home buyers</div><div>Over 50 lenders</div></div>
    <div class="loan-col"><h3>INVESTMENT LOAN</h3><div>Property investment loans</div><div>Interest only loans</div></div>
    <div class="loan-col"><h3>REFINANCING</h3><div>Refinancing for the best rate</div><div>Upsizing or downsizing</div><div>Change from a variable to a fixed rate</div></div>
    <div class="loan-col"><h3>BUSINESS LOAN</h3><div>Long term</div><div>Short term</div><div>Equipment and leasing</div></div>
  </div>
</section>

<section class="contact-band">
  <div class="contact-lead">
    <span class="phone-icon"><svg width="14" height="14" viewBox="0 0 24 24"><path fill="#fff" d="M6.6 10.8a15 15 0 0 0 6.6 6.6l2.2-2.2c.3-.3.7-.4 1-.2 1.1.4 2.3.6 3.6.6.6 0 1 .4 1 1V20c0 .6-.4 1-1 1A17 17 0 0 1 3 4c0-.6.4-1 1-1h3.5c.6 0 1 .4 1 1 0 1.3.2 2.5.6 3.6.1.3 0 .7-.2 1z"/></svg></span>
    <h2>Contact Brightwell Lending today on 1800 555 214 to find out more.</h2>
  </div>
  <p class="contact-text">There are many different loan products in the marketplace. Brightwell Lending has access to a wide panel of lenders which means we can access bank and non-bank lenders that meet the individual needs of our customers.</p>
  <form class="calculator">
    <h4>LOAN CALCULATOR</h4>
    <div class="calc-row"><label>Loan amount</label><span class="unit">$</span><span class="field wide"></span></div>
    <div class="calc-row"><label>Loan term</label><span class="unit"></span><span class="field"></span><small>year, or</small><span class="field"></span><small>months</small></div>
    <div class="calc-row"><label>Interest rate</label><span class="unit">%</span><span class="field wide"></span><small>per year</small></div>
    <div class="calc-row"><label>Monthly payments</label><span class="unit">$</span><span class="field wide"></span></div>
    <span class="btn-dark">CALCULATE</span>
  </form>
</section>

<section class="featured">
  <h3>FEATURED IN:</h3>
  <div class="partners">
    <span class="partner">Tallyo</span>
    <span class="partner">Kestrel</span>
    <span class="partner">Norvanta</span>
    <span class="partner">Soundloft</span>
  </div>
</section>

<footer class="site-footer">
  <p class="copyright">Copyright © 2012 Brightwell Lending. All rights reserved.</p>
  <div class="social"><span></span><span></span><span></span></div>
</footer>
</body>
</html>
```